Webdesign für Blog zum Thema KINDERWUNSCH
Zielgruppe
Hallo, ich bin 41 Jahre alt und lebe mit meinem Mann und unseren beiden Kindern (und Hund Ki;)) in einem kleinen Ort im Rhein-Main-Gebiet.
Ich musste auf meine beiden Kinder jeweils lange warten und diese schwere Zeit habe ich nicht vergessen. Meine beste Freundin hat mich irgendwann dazu überredet, anderen Frauen, denen es ähnlich geht, zu helfen. Besonders kann ich mich daran erinnern, wie schwer es war, verlässliche, gut recherchierte Quellen zum Thema Kinderwunsch zu finden.
Zusammen mit meiner besten Freundin baue ich daher einen Blog auf, bei dem es genau um diese Themen gehen soll.
Zielgruppe:
• Frauen
• Mitte / Ende 30
• Verheiratet, keine Kinder
• Höheres Bildungsniveau / nicht zwingend Akademiker
Kernemotionen:
o grübelt / ist unsicher
o nimmt ungewollte Kinderlosigkeit persönlich
o ängstlich / teils verzweifelt
o ungeduldig
Aufgabenstellung
Es geht um das Design unseres Blogs.
Uns ist besonders wichtig, dass der Blog das Spannungsverhältnis Seriosität – Freude – Ruhe vermittelt.
Das Design soll folgendes transportieren:
• Seriös / glaubwürdig
• Hochwertig
• Sicherheit / Ruhe / Seelenfriede
• Hoffnung
• Positiv / herzlich / unbeschwert – aber dennoch ernsthaft
ZUM FARBKONZEPT ETC. SIEHE BITTE BRIEFING ANBEI

```html
<!DOCTYPE html>
<html lang="de">
<head>
<meta charset="utf-8">
<title>Kinderwunsch Blog</title>
<link href="https://fonts.googleapis.com/css2?family=Asap:wght@400;500;600&display=swap" rel="stylesheet">
<style>
  :root {
    --teal: #5eb8c4;
    --teal-light: #7cc6cf;
    --teal-pale: #dff0f2;
    --teal-border: #b9e0e5;
    --ink: #2b2b2b;
    --muted: #8a8a8a;
    --white: #ffffff;
  }
  * { margin: 0; padding: 0; box-sizing: border-box; }
  html, body { width: 1200px; height: 800px; overflow: hidden; background: var(--white); }
  body { font-family: 'Asap', sans-serif; color: var(--ink); position: relative; }

  .top-rule {
    position: absolute; left: 0; top: 1px; width: 800px; height: 4px;
    background: repeating-linear-gradient(90deg, var(--teal) 0 5px, transparent 5px 8px);
  }

  .newsletter {
    position: absolute; left: 51px; top: 12px; width: 670px; height: 97px;
    background: var(--teal); color: var(--white);
  }
  .newsletter__title { position: absolute; left: 20px; top: 24px; font-size: 15.5px; font-weight: 500; }
  .newsletter__text { position: absolute; left: 20px; top: 49px; width: 290px; font-size: 10px; line-height: 12.5px; }
  .newsletter__input {
    position: absolute; left: 361px; top: 37px; width: 206px; height: 38px;
    background: var(--teal-light); color: #c9e9ed; font-size: 11px;
    padding-left: 13px; line-height: 38px;
  }
  .newsletter__button {
    position: absolute; left: 567px; top: 37px; width: 79px; height: 38px;
    background: var(--white); color: var(--teal); font-size: 12px; font-weight: 600;
    text-align: center; line-height: 38px;
  }

  .date-label { position: absolute; left: 51px; top: 130px; font-size: 15px; font-weight: 500; }

  .post { position: absolute; left: 51px; width: 670px; height: 210px; }
  .post__image {
    position: absolute; left: 0; top: 0; width: 208px; height: 167px; border-radius: 3px;
    background: linear-gradient(135deg, #c9a98a 0%, #8b6a55 40%, #d97a5a 75%, #e8b79a 100%);
  }
  .post__title {
    position: absolute; left: 246px; top: 0; width: 400px;
    font-size: 21.5px; line-height: 25px; font-weight: 600; color: var(--teal);
  }
  .post__subtitle { position: absolute; left: 246px; top: 52px; font-size: 14.5px; font-weight: 500; }
  .post__body {
    position: absolute; left: 246px; top: 86px; width: 425px;
    font-size: 11.8px; line-height: 14.2px; color: var(--muted); text-align: justify;
  }
  .post__more {
    position: absolute; left: 246px; top: 199px; width: 168px; height: 42px;
    border: 1px solid var(--teal-border); padding: 2px;
  }
  .post__more span {
    display: flex; align-items: center; justify-content: space-between;
    height: 100%; background: var(--teal); color: var(--white);
    font-size: 14px; font-weight: 500; padding: 0 14px 0 16px;
  }

  .pagination { position: absolute; left: 320px; top: 732px; display: flex; align-items: center; }
  .pagination__page {
    width: 40px; height: 40px; margin-right: 6px; border: 1px solid var(--teal-border); padding: 2px;
  }
  .pagination__page span {
    display: block; height: 100%; background: var(--teal-pale); color: var(--teal);
    font-size: 13px; font-weight: 600; text-align: center; line-height: 34px;
  }
  .pagination__page--current span { background: var(--teal); color: var(--white); }
  .pagination__next { margin-left: 10px; font-size: 11.5px; color: var(--teal); font-weight: 500; }

  .hero-photo {
    position: absolute; left: 800px; top: 0; width: 400px; height: 800px;
    background: linear-gradient(180deg, #f3d9c0 0%, #d9a58a 25%, #a8b07a 50%, #6e9b3e 75%, #5a8a2e 100%);
  }
</style>
</head>
<body>
  <div class="top-rule"></div>

  <section class="newsletter">
    <h2 class="newsletter__title">Newsletter abonnieren</h2>
    <p class="newsletter__text">Wenn Du keinen Artikel mehr verpassen möchtest, dann benachrichtige ich Dich gerne per E-Mail.</p>
    <div class="newsletter__input">E-Mail-Adresse eingeben</div>
    <div class="newsletter__button">Senden</div>
  </section>

  <p class="date-label">vor 2 Wochen</p>

  <article class="post" style="top:165px">
    <div class="post__image" role="img" aria-label="Foto: drei Freundinnen sitzen lachend mit Kaffeebechern an einem Tisch"></div>
    <h3 class="post__title">Freunde sind das Fundament für deinen Wunsch nach Kindern</h3>
    <p class="post__subtitle">Ich erzähle Dir, wie mir eine Freundin helfen konnte.</p>
    <p class="post__body">Lorem ipsum dolor sit amet, consetetur sadipscing elitr, sed diam nonumy eirmod tempor invidunt ut labore et dolore magna aliquyam erat, sed diam voluptua. At vero eos et accusam et justo duo dolores et ea rebum. Stet clita kasd gubergren, no sea takimata sanctus est Lorem ipsum dolor sit amet. Lorem ipsum dolor sit amet, consetetur sadipscing elitr, sed diam nonumy eirmod tempor invidunt ut labore et dolore magna aliquyam erat, sed diam voluptua.</p>
    <div class="post__more"><span>Weiterlesen
      <svg width="16" height="12" viewBox="0 0 16 12"><path d="M0 4.5h9V0l7 6-7 6V7.5H0z" fill="#fff"/></svg></span></div>
  </article>

  <article class="post" style="top:438px">
    <div class="post__image" role="img" aria-label="Foto: drei Freundinnen sitzen lachend mit Kaffeebechern an einem Tisch"></div>
    <h3 class="post__title">Freunde sind das Fundament für deinen Wunsch nach Kindern</h3>
    <p class="post__subtitle">Ich erzähle Dir, wie mir eine Freundin helfen konnte.</p>
    <p class="post__body">Lorem ipsum dolor sit amet, consetetur sadipscing elitr, sed diam nonumy eirmod tempor invidunt ut labore et dolore magna aliquyam erat, sed diam voluptua. At vero eos et accusam et justo duo dolores et ea rebum. Stet clita kasd gubergren, no sea takimata sanctus est Lorem ipsum dolor sit amet. Lorem ipsum dolor sit amet, consetetur sadipscing elitr, sed diam nonumy eirmod tempor invidunt ut labore et dolore magna aliquyam erat, sed diam voluptua.</p>
    <div class="post__more" style="top:201px"><span>Weiterlesen
      <svg width="16" height="12" viewBox="0 0 16 12"><path d="M0 4.5h9V0l7 6-7 6V7.5H0z" fill="#fff"/></svg></span></div>
  </article>

  <nav class="pagination">
    <div class="pagination__page pagination__page--current"><span>1</span></div>
    <div class="pagination__page"><span>2</span></div>
    <div class="pagination__page"><span>3</span></div>
    <div class="pagination__page"><span>4</span></div>
    <span class="pagination__next">Weiter</span>
  </nav>

  <div class="hero-photo" role="img" aria-label="Foto: zwei Hände halten ein Paar kleine Babyschuhe vor grüner Wiese im Gegenlicht"></div>
</body>
</html>
```